Business Card Design

We are a manufacturing company that has been in business for over 30 years, established in 1981. We are looking to increase our business with defence force, government, and the major telecoms so the card needs to present the company as being cutting edge, secure, and professional.
Industry/Entity Type
Defence
Contact Information for Business Card
Name Gareth Olsund
Phone 02 9374 6815
Fax 02 9457 3162
mobile 0438260517
Email Gary@Korvex.com.au
Webiste www.korvex.com.au
ABN 58 006 391 842
address: 17 Belcor Street Harwood Vale NSW 2571
"Builder of Aerials, Navigation Units, Radar, Cable Harnesses, Signal, Defence, & Communication Systems"
Look and feel

```html
<!DOCTYPE html>
<html lang="en">
<head>
<meta charset="utf-8">
<title>Korvex Business Card</title>
<link rel="stylesheet" href="https://fonts.googleapis.com/css2?family=Open+Sans:wght@400;600&display=swap">
<style>
  :root {
    --stage: #ececec;
    --card-back: #d8d8d8;
    --card-front: #ffffff;
    --band-dark: #a2a2a2;
    --band-light: #dcdcdc;
    --navy: #1c2a5c;
    --rust: #c2432a;
    --ink: #2b2b2b;
    --muted: #6f6f6f;
    --peach: #f2cdb7;
  }
  * { box-sizing: border-box; margin: 0; padding: 0; }
  html, body { width: 1200px; height: 900px; overflow: hidden; }
  body {
    background: var(--stage);
    font-family: "Open Sans", Arial, sans-serif;
    position: relative;
  }
  .card {
    position: absolute;
    width: 560px;
    height: 330px;
    overflow: hidden;
    box-shadow: 0 6px 18px rgba(0,0,0,0.18);
  }

  /* Reverse side */
  .card--reverse { left: 60px; top: 90px; background: var(--card-back); }
  .brand-mark {
    position: absolute;
    display: flex;
    flex-direction: column;
    align-items: center;
    gap: 8px;
  }
  .brand-mark__square { background: var(--navy); }
  .brand-mark__name {
    color: var(--rust);
    font-weight: 600;
    letter-spacing: 2px;
    line-height: 1;
  }
  .card--reverse .brand-mark { left: 50%; top: 100px; transform: translateX(-50%); }
  .card--reverse .brand-mark__square { width: 88px; height: 88px; }
  .card--reverse .brand-mark__name { font-size: 17px; }
  .web-band {
    position: absolute;
    left: 0; right: 0; top: 262px; height: 34px;
    background: var(--band-dark);
    color: #fff;
    font-size: 18px;
    display: flex;
    align-items: center;
    justify-content: center;
    padding-left: 40px;
  }

  /* Front side */
  .card--front { left: 580px; top: 470px; background: var(--card-front); }
  .emblem-fade {
    position: absolute;
    right: 0; top: 0;
    width: 300px; height: 330px;
    background: linear-gradient(225deg, var(--peach) 0%, rgba(242,205,183,0.55) 45%, rgba(242,205,183,0) 80%);
  }
  .card--front .brand-mark { right: 42px; top: 34px; }
  .card--front .brand-mark__square { width: 96px; height: 84px; }
  .card--front .brand-mark__name { font-size: 15px; }
  .name-tag {
    position: absolute;
    left: 36px; top: 108px;
    background: var(--rust);
    color: #fff;
    font-size: 20px;
    padding: 3px 14px;
    letter-spacing: 0.5px;
  }
  .contact-list {
    position: absolute;
    left: 36px; top: 154px;
    list-style: none;
    border-left: 1px solid var(--ink);
    padding-left: 0;
  }
  .contact-list li {
    display: flex;
    align-items: center;
    height: 17px;
    font-size: 12.5px;
    color: var(--ink);
    position: relative;
    padding-left: 12px;
    white-space: nowrap;
  }
  .contact-list svg {
    position: absolute;
    left: -20px;
    width: 11px; height: 11px;
    fill: var(--ink);
  }
  .abn {
    position: absolute;
    right: 30px; top: 258px;
    font-size: 10px;
    color: var(--ink);
  }
  .tagline-band {
    position: absolute;
    left: 0; right: 0; top: 278px; height: 44px;
    background: linear-gradient(90deg, var(--band-light) 0%, #e6e6e6 70%, rgba(230,230,230,0.4) 100%);
    color: var(--muted);
    font-size: 13px;
    line-height: 17px;
    text-align: center;
    padding-top: 5px;
    white-space: nowrap;
  }
</style>
</head>
<body>

<section class="card card--reverse" aria-label="Card reverse">
  <div class="brand-mark">
    <div class="brand-mark__square"></div>
    <div class="brand-mark__name">KORVEX</div>
  </div>
  <div class="web-band">www.korvex.com.au</div>
</section>

<section class="card card--front" aria-label="Card front">
  <div class="emblem-fade" role="img" aria-label="Faint layered brand emblem decoration in soft peach tones"></div>
  <div class="brand-mark">
    <div class="brand-mark__square"></div>
    <div class="brand-mark__name">KORVEX</div>
  </div>

  <div class="name-tag">GARETH OLSUND</div>

  <ul class="contact-list">
    <li><svg viewBox="0 0 12 12"><path d="M1 4c0-2 2-3 5-3s5 1 5 3v1H8V4H4v1H1zM2 6h8l1 5H1z"/></svg>02 9374 6815</li>
    <li><svg viewBox="0 0 12 12"><path d="M3 0h6v12H3zM4 1v8h4V1z"/></svg>0438260517</li>
    <li><svg viewBox="0 0 12 12"><path d="M3 0h6v4H3zM1 5h10v5H1zM3 9h6v3H3z"/></svg>02 9457 3162</li>
    <li><svg viewBox="0 0 12 12"><path d="M6 0a6 6 0 1 1 0 12A6 6 0 0 1 6 0zM3 4v4h6V4zM3.5 4.5 6 6.5 8.5 4.5"/></svg>Gary@Korvex.com.au</li>
    <li><svg viewBox="0 0 12 12"><path d="M6 1 0 6h2v5h3V8h2v3h3V6h2z"/></svg>17 Belcor Street, Harwood Vale, NSW 2571</li>
  </ul>

  <div class="abn">ABN 58 006 391 842</div>

  <div class="tagline-band">Builder of Aerials, Navigation Units, Radar, Cable Harnesses,<br>Signal, Defence, &amp; Communication Systems"</div>
</section>

</body>
</html>
```